Deactivated Coal-Fired Power Plant to be redeveloped into a Green Energy Campus.

Want a striking business card statement that introduces our concept project to provide economic and community recovery to a former rural coal community in western PA.
Essentially 12 project representatives that will lead both the demolition of an existing power plant and the redevelopment to a new Green energy site.
Business Card should reflect our effort.
We are open to ideas.

Target Market(s)

Energy and Power Generation industries

Industry/Entity Type

Power Generation and Data Centers

Contact Information for Business Card

Included in uploaded materials

Font styles to use
Sans Serif
Other font styles liked:
• Arial, Calibri

Requirements
Must have
• Multiple colors

```html
<!DOCTYPE html>
<html lang="en">
<head>
<meta charset="utf-8">
<title>Ridgeline Renewal – Business Card</title>
<link rel="stylesheet" href="https://fonts.googleapis.com/css2?family=Roboto:wght@400;700;900&display=swap">
<style>
  :root {
    --stage: #3b3b3b;
    --card-white: #ffffff;
    --card-black: #161616;
    --ink: #111111;
    --muted: #333333;
    --green: #1e9646;
    --pattern-dark: #0c0c0c;
    --pattern-light: #3c3c3c;
  }
  * { margin: 0; padding: 0; box-sizing: border-box; }
  html, body {
    width: 1200px; height: 801px; overflow: hidden;
    background: var(--stage);
    font-family: "Roboto", Arial, sans-serif;
  }
  .stage {
    position: relative; width: 1200px; height: 801px;
    display: flex; align-items: center; justify-content: center; gap: 50px;
  }
  .card {
    position: relative; width: 525px; height: 300px;
    border-bottom: 4px solid var(--green);
    box-shadow: 0 14px 30px rgba(0,0,0,.35);
  }
  .card-front { background: var(--card-white); }
  .card-back { background: var(--card-black); overflow: hidden; }

  /* front */
  .brand {
    position: absolute; top: 36px; right: 48px;
    display: flex; align-items: center; gap: 10px;
  }
  .brand-dot { width: 46px; height: 46px; border-radius: 50%; background: var(--green); }
  .brand-name {
    font-weight: 900; font-size: 26px; line-height: 1; color: var(--ink);
    text-transform: uppercase; letter-spacing: .5px;
  }
  .divider {
    position: absolute; left: 32px; right: 48px; top: 120px;
    height: 1.5px; background: var(--green);
  }
  .holder { position: absolute; left: 32px; top: 150px; }
  .holder-name {
    font-weight: 900; font-size: 24px; color: var(--ink);
    text-transform: uppercase; letter-spacing: .3px;
  }
  .holder-title { font-size: 16px; color: var(--green); margin-top: 2px; }
  .contacts { list-style: none; margin-top: 16px; }
  .contacts li {
    display: flex; align-items: center; gap: 8px;
    font-size: 15px; color: var(--muted); line-height: 1.45;
  }
  .contacts svg { width: 13px; height: 13px; flex: none; }
  .entity {
    position: absolute; right: 48px; bottom: 104px;
    font-size: 14px; color: var(--ink);
  }

  /* back */
  .pattern-field {
    position: absolute; inset: 0;
    background: linear-gradient(120deg, var(--pattern-dark) 0%, #1b1b1b 50%, var(--pattern-light) 100%);
  }
  .back-mark {
    position: absolute; right: 70px; top: 170px;
    display: flex; align-items: center; gap: 8px;
  }
  .back-mark .brand-dot { width: 30px; height: 30px; }
  .back-mark .brand-name { color: #ffffff; font-size: 16px; }
</style>
</head>
<body>
<main class="stage">
  <section class="card card-front" aria-label="Business card front">
    <div class="brand">
      <span class="brand-dot"></span>
      <span class="brand-name">Ridgeline Renewal</span>
    </div>
    <div class="divider"></div>
    <div class="holder">
      <h1 class="holder-name">Daniel Marsh</h1>
      <p class="holder-title">Chief Operating Officer</p>
      <ul class="contacts">
        <li>
          <svg viewBox="0 0 12 12"><rect x="3" y="1" width="6" height="10" rx="1" fill="none" stroke="#1e9646" stroke-width="1.3"/></svg>
          555-014-2200
        </li>
        <li>
          <svg viewBox="0 0 12 12"><path d="M2 2 L4.5 1.5 L5.5 4 L4 5 Q5.5 7.5 7 8 L8 6.5 L10.5 7.5 L10 10 Q4 10 2 2Z" fill="#1e9646"/></svg>
          555-014-2200
        </li>
        <li>
          <svg viewBox="0 0 12 12"><rect x="1" y="3" width="10" height="7" fill="#1e9646"/><path d="M1 3 L6 7 L11 3" fill="none" stroke="#fff" stroke-width="1"/></svg>
          dmarsh@ridgelinerenewal.com
        </li>
      </ul>
    </div>
    <p class="entity">Ridgeline Renewal LLC</p>
  </section>

  <section class="card card-back" aria-label="Business card back">
    <div class="pattern-field" role="img" aria-label="Repeating tonal pattern of the brand symbol on black"></div>
    <div class="back-mark">
      <span class="brand-dot"></span>
      <span class="brand-name">Ridgeline Renewal</span>
    </div>
  </section>
</main>
</body>
</html>
```